Plimbo advertising imagery for a 13.28kW solar system

Project Overview:
We are thrilled to announce a limited-time offer on our top-of-the-line 13.28kW Solar System! This Plimbo ad campaign aims to generate excitement and interest among homeowners and businesses looking to harness the power of solar energy. The special offer includes a competitively priced 13.28kW solar system starting from $5800, fully installed, and an exclusive free upgrade to the Velmarq 10kW 1 Phase inverter for a limited two-week period.

Target Audience:
Our target audience consists of environmentally conscious homeowners, small to medium-sized businesses, and those seeking to reduce their energy bills and carbon footprint. We will be focusing on customers in [your service area location] or nearby regions, aged between 25 to 65 years old.

Key Message:
The advertisement should convey the following key messages:

"Go Solar and Save Big on Your Energy Bills!"
"Upgrade to the Powerful Velmarq Inverter for Free - Limited Time Only!"
"High-Performance 13.28kW Solar System Fully Installed from $5800."
"Harness Clean and Renewable Energy to Power Your Home or Business."
Design Requirements:

Dimensions: The advertisement should comply with Plimbo's recommended ad dimensions (e.g., 1200 x 628 pixels).
Branding: Incorporate our company logo and colors (Logo attached).
Visuals: Use eye-catching images or animations that showcase solar panels, clean energy, and happy customers enjoying the benefits of solar power.
Call-to-Action (CTA): Include a prominent CTA button, such as "Get a Quote," "Limited Time Offer - Act Now!" or "Learn More."
Text: Keep the text clear, concise, and persuasive, highlighting the savings, eco-friendliness, and exclusive offer.
Pricing Details: Clearly mention the starting price of the 13.28kW solar system and emphasize the free upgrade to the Velmarq 10kW 1 Phase inverter.
Trust Signals: Incorporate any relevant awards, certifications, or customer testimonials to build trust and credibility.
Countdown Timer (Optional): Consider adding a countdown timer to create a sense of urgency and remind viewers about the limited-time offer.
Additional Information:

Include the following contact information: Website URL, phone number, and email address.
The advertisement should comply with Plimbo's advertising guidelines and policies.
Prominently display the duration of the offer: "Two Weeks Only - Act Fast!"

Target Market(s)

Industry/Entity Type

Solar Energy

Colors
0054AA
0677BA
7BADD7
CADEEF
E8F1F8

Requirements
Must have
• Key Message: The advertisement should convey the following key messages: "Go Solar and Save Big on Your Energy Bills!" "Upgrade to the Powerful Velmarq Inverter for Free - Limited Time Only!" "High-Performance 13.28kW Solar System Fully Installed from $5800." "Harness Clean and Renewable Energy to Power Your Home or Business."
Nice to have
• Must have picture of solar panels and the Velmarq 10kW 1 Phase inverter

```html
<!DOCTYPE html>
<html lang="en">
<head>
<meta charset="utf-8">
<title>Tarvo Energy – 13.28kW Solar Offer</title>
<link rel="stylesheet" href="https://fonts.googleapis.com/css2?family=Montserrat:wght@400;500;600;700;800&family=Bebas+Neue&display=swap">
<style>
  :root{
    --red:#c0232b;
    --slate:#3d4049;
    --white:#ffffff;
    --ink:#2f3138;
    --tick:#3bb54a;
    --page:#e4e4e4;
    --sky-top:#3d8fd8;
    --sky-mid:#a9cdea;
    --panel-deep:#0f2f73;
  }
  html,body{margin:0;padding:0;width:1200px;height:1200px;overflow:hidden;background:var(--page);}
  body{font-family:"Montserrat",sans-serif;}
  .stage{position:absolute;left:0;top:287px;width:1226px;height:640px;transform:scale(0.9788);transform-origin:0 0;}
  .ad{position:relative;width:1226px;height:640px;overflow:hidden;background:var(--slate);}
  .ad-bg{position:absolute;inset:0;}
  .brand{position:absolute;left:52px;top:62px;display:flex;align-items:center;gap:14px;}
  .brand-dot{width:26px;height:26px;border-radius:50%;background:var(--red);}
  .brand-name{font-weight:700;font-size:38px;line-height:44px;color:var(--red);letter-spacing:0.5px;white-space:nowrap;}
  .brand-tagline{position:absolute;left:52px;top:128px;font-size:14px;color:var(--ink);letter-spacing:0.2px;}
  .offer{position:absolute;color:var(--white);}
  .offer-lead{left:18px;top:205px;width:103px;text-align:right;font-size:15px;font-weight:500;line-height:21px;}
  .offer-size{left:128px;top:196px;font-size:46px;font-weight:800;letter-spacing:-1px;}
  .offer-note{left:339px;top:203px;font-size:15px;font-weight:600;line-height:22px;}
  .offer-price{left:128px;top:250px;font-size:20px;font-weight:500;}
  .offer-price strong{font-size:46px;font-weight:800;letter-spacing:-0.5px;vertical-align:-6px;}
  .benefits{position:absolute;left:50px;top:338px;margin:0;padding:0;list-style:none;color:var(--white);font-size:18px;line-height:25px;width:420px;}
  .benefits li{position:relative;padding-left:21px;margin-bottom:11px;}
  .benefits li::before{content:"";position:absolute;left:0;top:8px;width:11px;height:11px;border-radius:50%;background:var(--tick);}
  .benefits strong{font-weight:700;}
  .urgency{position:absolute;left:60px;top:508px;font-family:"Bebas Neue",sans-serif;font-size:48px;color:var(--white);letter-spacing:0.5px;}
  .cta-bar{position:absolute;left:46px;top:568px;width:454px;height:38px;border-radius:19px;background:var(--red);display:flex;align-items:center;justify-content:center;gap:8px;color:var(--white);font-size:13px;font-weight:700;}
  .cta-bar span::before{content:"»";font-size:18px;margin-right:7px;}
  .phone{position:absolute;left:882px;top:512px;width:270px;height:46px;border-radius:23px;background:var(--red);display:flex;align-items:center;gap:10px;color:var(--white);font-size:26px;font-weight:700;padding-left:10px;box-sizing:border-box;}
  .phone-icon{width:30px;height:30px;border-radius:50%;background:var(--white);display:flex;align-items:center;justify-content:center;}
  .contact{position:absolute;left:887px;display:flex;align-items:center;gap:8px;color:var(--white);font-size:18px;}
  .contact strong{font-weight:700;}
  .contact-web{top:566px;}
  .contact-mail{top:594px;}
</style>
</head>
<body>
<div class="stage">
  <section class="ad">
    <svg class="ad-bg" width="1226" height="640" viewBox="0 0 1226 640">
      <defs>
        <linearGradient id="photoTones" x1="0" y1="0" x2="0" y2="1">
          <stop offset="0" stop-color="var(--sky-top)"/>
          <stop offset="0.32" stop-color="var(--sky-mid)"/>
          <stop offset="0.42" stop-color="#5d6f86"/>
          <stop offset="0.55" stop-color="#1d4795"/>
          <stop offset="1" stop-color="var(--panel-deep)"/>
        </linearGradient>
      </defs>
      <polygon points="0,0 398,0 455,184 0,184" fill="var(--white)"/>
      <polygon points="0,184 455,184 492,312 0,312" fill="var(--red)"/>
      <path role="img" aria-label="Rooftop solar panels on a red metal roof with a city skyline under blue sky"
            d="M398,0 H1226 V392 L700,555 Q640,575 590,555 Q560,540 545,505 Z" fill="url(#photoTones)"/>
    </svg>

    <div class="brand">
      <div class="brand-dot"></div>
      <div class="brand-name">TARVO ENERGY</div>
    </div>
    <div class="brand-tagline">RESIDENTIAL AND COMMERCIAL SOLAR POWER</div>

    <div class="offer offer-lead">High-<br>Performance</div>
    <div class="offer offer-size">13.28kW</div>
    <div class="offer offer-note">Solar System<br>Fully Installed</div>
    <div class="offer offer-price">from <strong>$5800</strong></div>

    <ul class="benefits">
      <li>Go Solar and Save Big on Your Energy Bills!</li>
      <li>Harness Clean and Renewable Energy to Power Your Home or Business.</li>
      <li>Upgrade to the Powerful Velmarq Inverter for <strong>Free - Limited Time Only!</strong></li>
    </ul>

    <div class="urgency">Two Weeks Only - Act Fast!</div>
    <div class="cta-bar"><span>Get a Quote</span><span>Limited Time Offer - Act Now!</span><span>Learn More</span></div>

    <div class="phone">
      <span class="phone-icon">
        <svg width="18" height="18" viewBox="0 0 24 24"><path d="M6.6 10.8a15 15 0 0 0 6.6 6.6l2.2-2.2a1 1 0 0 1 1-.25 11.4 11.4 0 0 0 3.6.57 1 1 0 0 1 1 1V20a1 1 0 0 1-1 1A17 17 0 0 1 3 4a1 1 0 0 1 1-1h3.5a1 1 0 0 1 1 1c0 1.25.2 2.45.57 3.6a1 1 0 0 1-.25 1z" fill="var(--red)"/></svg>
      </span>
      +61 7 3040 5862
    </div>
    <div class="contact contact-web">
      <svg width="20" height="20" viewBox="0 0 20 20" fill="none" stroke="var(--white)" stroke-width="1.3"><circle cx="10" cy="10" r="8"/><ellipse cx="10" cy="10" rx="3.5" ry="8"/><path d="M2 10h16M3.5 6h13M3.5 14h13"/></svg>
      <span>www.<strong>tarvoenergy</strong>.com.au</span>
    </div>
    <div class="contact contact-mail">
      <svg width="20" height="20" viewBox="0 0 20 20"><circle cx="10" cy="10" r="8.5" fill="none" stroke="var(--white)" stroke-width="1.3"/><rect x="5.5" y="7" width="9" height="6" rx="0.8" fill="var(--white)"/><path d="M5.5 7.3l4.5 3.2 4.5-3.2" stroke="var(--slate)" stroke-width="1" fill="none"/></svg>
      <span>info@<strong>tarvoenergy</strong>.com.au</span>
    </div>
  </section>
</div>
</body>
</html>
```